The Pixel Tavern Business card.

A Simple card with our Logo and contact information. To give to investors and other professionals.

We are a nerd themed bar.
our target market is young professionals age 21+ but the real purpose of this business card is to present to potential investors and other professionals with our contact information. as we are still looking for funding before we start up.

I am partial to green and my partner likes red we are open to iteration.

Target Market(s)

Investors

Industry/Entity Type

Business

Contact Information for Business Card

Marcus Henley (555) 730-6621 kent.w4100@mailbox-demo.net Dalton Vrease (555) 918-2047 daltonv731@mailbox-demo.net

Font styles to use
Serif

Requirements
Nice to have
• Keep it simple but not boring.
• Use the Logos but feel free to edit them to match theme/colors.
• Keep the back clean and use one of the Logos.

```html
<!DOCTYPE html>
<html lang="en">
<head>
<meta charset="utf-8">
<title>The Pixel Tavern – Business Card</title>
<link rel="stylesheet" href="https://fonts.googleapis.com/css2?family=Arimo:wght@400;700&display=swap">
<style>
  :root {
    --stage: #e9e6e1;
    --card-black: #0b0b0b;
    --card-white: #f7f7f5;
    --accent-red: #e0161f;
    --ink: #111111;
    --paper-text: #ffffff;
    --muted: #d6d6d6;
    --divider: #5a5a5a;
  }
  * { margin: 0; padding: 0; box-sizing: border-box; }
  html, body {
    width: 1200px; height: 1023px; overflow: hidden;
    background: var(--stage);
    font-family: "Arimo", Arial, sans-serif;
  }
  .stage {
    width: 1200px; height: 1023px;
    display: flex; flex-direction: column; align-items: center;
    justify-content: center; gap: 83px;
  }
  .card {
    position: relative; width: 700px; height: 400px; overflow: hidden;
    box-shadow: 0 10px 28px rgba(0,0,0,.25);
  }
  /* Front */
  .card-front { background: var(--card-white); }
  .front-shape { position: absolute; inset: 0; }
  .brand { display: flex; align-items: center; gap: 14px; }
  .card-front .brand { position: absolute; left: 70px; top: 92px; }
  .brand-dot {
    width: 26px; height: 26px; border-radius: 50%; background: var(--accent-red); flex: none;
  }
  .brand-name {
    font-weight: 700; font-size: 46px; letter-spacing: 1px;
    text-transform: uppercase; color: var(--ink); white-space: nowrap;
  }
  .contacts {
    position: absolute; left: 0; right: 0; top: 282px;
    display: flex; color: var(--paper-text);
  }
  .contact { width: 350px; padding-left: 44px; }
  .contact + .contact { border-left: 1px solid var(--divider); padding-left: 36px; }
  .contact-name { font-size: 22px; font-weight: 700; }
  .contact-role { font-size: 14px; color: var(--muted); margin: 2px 0 12px; }
  .contact-line {
    display: flex; align-items: center; gap: 8px;
    font-size: 14px; line-height: 22px; color: var(--paper-text); white-space: nowrap;
  }
  .contact-line svg { width: 14px; height: 14px; flex: none; }
  /* Back */
  .card-back { background: var(--card-black); }
  .brand-block {
    position: absolute; inset: 0; display: flex; flex-direction: column;
    align-items: center; justify-content: center;
  }
  .card-back .brand-name { color: var(--paper-text); font-size: 44px; }
  .tagline {
    margin-top: 10px; font-size: 15px; letter-spacing: 4px;
    color: var(--paper-text); text-transform: uppercase;
  }
</style>
</head>
<body>
<main class="stage">

  <section class="card card-front" aria-label="Business card front">
    <svg class="front-shape" viewBox="0 0 700 400" aria-hidden="true">
      <path d="M0 238 Q350 246 700 100 L700 400 L0 400 Z" fill="var(--accent-red)"/>
      <path d="M0 245 Q350 253 700 110 L700 400 L0 400 Z" fill="var(--card-white)"/>
      <path d="M0 250 Q350 260 700 118 L700 400 L0 400 Z" fill="var(--card-black)"/>
    </svg>

    <div class="brand">
      <span class="brand-dot"></span>
      <span class="brand-name">The Pixel Tavern</span>
    </div>

    <div class="contacts">
      <div class="contact">
        <p class="contact-name">Dalton Vrease</p>
        <p class="contact-role">Founder</p>
        <p class="contact-line">
          <svg viewBox="0 0 14 14"><rect x="1" y="1" width="12" height="12" rx="1.5" fill="#fff"/><rect x="3" y="3" width="8" height="3" fill="#0b0b0b"/><rect x="3" y="8" width="2" height="1.5" fill="#0b0b0b"/><rect x="6" y="8" width="2" height="1.5" fill="#0b0b0b"/><rect x="9" y="8" width="2" height="1.5" fill="#0b0b0b"/></svg>
          (555) 918-2047 (Dalton Vrease)
        </p>
        <p class="contact-line">
          <svg viewBox="0 0 14 14"><rect x="1" y="3" width="12" height="8" fill="#fff"/><path d="M1 3 L7 8 L13 3" fill="none" stroke="#0b0b0b" stroke-width="1"/></svg>
          daltonv731@mailbox-demo.net
        </p>
      </div>
      <div class="contact">
        <p class="contact-name">Marcus Henley</p>
        <p class="contact-role">Founder</p>
        <p class="contact-line">
          <svg viewBox="0 0 14 14"><rect x="1" y="1" width="12" height="12" rx="1.5" fill="#fff"/><rect x="3" y="3" width="8" height="3" fill="#0b0b0b"/><rect x="3" y="8" width="2" height="1.5" fill="#0b0b0b"/><rect x="6" y="8" width="2" height="1.5" fill="#0b0b0b"/><rect x="9" y="8" width="2" height="1.5" fill="#0b0b0b"/></svg>
          (555) 730-6621 (Marcus Henley)
        </p>
        <p class="contact-line">
          <svg viewBox="0 0 14 14"><rect x="1" y="3" width="12" height="8" fill="#fff"/><path d="M1 3 L7 8 L13 3" fill="none" stroke="#0b0b0b" stroke-width="1"/></svg>
          kent.w4100@mailbox-demo.net
        </p>
      </div>
    </div>
  </section>

  <section class="card card-back" aria-label="Business card back">
    <div class="brand-block">
      <div class="brand">
        <span class="brand-dot"></span>
        <span class="brand-name">The Pixel Tavern</span>
      </div>
      <p class="tagline">Lounge and Arcade</p>
    </div>
  </section>

</main>
</body>
</html>
```